Corvath Properties Business Card Design

We would now like to design business cards with the new Corvath Properties logo

Target Market(s)

Professional

Industry/Entity Type

Professional services

Contact Information for Business Card

Employee name, title, phone number, email address, corporate office address and logo.

Font styles to use
Sans Serif

Colors
0054AA
0677BA
7BADD7
CADEEF
E8F1F8

Requirements
Must have
• My logo
Should not have
• any other pictures or images besides my logo

```html
<!DOCTYPE html>
<html lang="en">
<head>
<meta charset="utf-8">
<title>Corvath Properties Business Card</title>
<link rel="stylesheet" href="https://fonts.googleapis.com/css2?family=Open+Sans:wght@400;600;700&display=swap">
<style>
  :root {
    --brand-deep: #0054AA;
    --brand-blue: #2F74B8;
    --brand-mid: #0677BA;
    --brand-light: #7BADD7;
    --brand-pale: #CADEEF;
    --card-white: #F7F8F9;
    --text-grey: #4A4A4A;
    --rule-grey: #555555;
    --backdrop: #2A2B2C;
  }
  * { margin: 0; padding: 0; box-sizing: border-box; }
  html, body {
    width: 1200px; height: 900px; overflow: hidden;
    background: var(--backdrop);
    font-family: "Open Sans", Arial, sans-serif;
  }
  .stage { position: relative; width: 1200px; height: 900px; }

  .card {
    position: absolute;
    width: 630px; height: 360px;
    border-radius: 4px;
    box-shadow: 0 18px 40px rgba(0,0,0,0.45);
    overflow: hidden;
  }

  /* Front */
  .card-front {
    left: 90px; top: 60px;
    background: var(--brand-blue);
    display: flex; align-items: center; justify-content: center;
  }
  .card-front .brand-name {
    color: #FFFFFF;
    font-weight: 700;
    font-size: 40px;
    letter-spacing: 1px;
    display: flex; align-items: center; gap: 16px;
  }
  .brand-mark {
    display: inline-block; width: 26px; height: 26px;
    background: currentColor;
  }

  /* Back */
  .card-back {
    left: 480px; top: 480px;
    background: var(--card-white);
    display: flex; align-items: center;
    padding: 0 38px;
  }
  .card-back .brand-name {
    color: var(--brand-blue);
    font-weight: 700;
    font-size: 28px;
    line-height: 1.15;
    width: 235px;
    display: flex; align-items: center; gap: 12px;
  }
  .divider {
    width: 1px; height: 170px;
    background: var(--rule-grey);
    margin: 0 26px 0 10px;
  }
  .contact { color: var(--text-grey); font-size: 15px; }
  .contact .role { font-size: 15px; }
  .contact .person {
    color: var(--brand-blue);
    font-weight: 700;
    font-size: 20px;
    letter-spacing: 0.5px;
    margin-bottom: 12px;
  }
  .contact-list { list-style: none; }
  .contact-list li {
    display: flex; align-items: flex-start; gap: 10px;
    line-height: 1.45; margin-bottom: 3px;
  }
  .contact-list svg {
    width: 15px; height: 15px; flex: none; margin-top: 4px;
    fill: var(--brand-blue);
  }
</style>
</head>
<body>
<main class="stage">

  <section class="card card-front" aria-label="Business card front">
    <div class="brand-name"><span class="brand-mark"></span>Corvath Properties</div>
  </section>

  <section class="card card-back" aria-label="Business card back">
    <div class="brand-name"><span class="brand-mark"></span><span>Corvath<br>Properties</span></div>
    <div class="divider"></div>
    <div class="contact">
      <p class="role">Director</p>
      <p class="person">ELENA MARSH</p>
      <ul class="contact-list">
        <li>
          <svg viewBox="0 0 16 16" aria-hidden="true"><path d="M3.5 1 6 1.5 7 5 5.3 6.3c.8 1.8 2.3 3.3 4.2 4.3L11 9l3.5 1 .5 2.5-2 2C7 14 2 9 1.5 3z"/></svg>
          <span>0412558903</span>
        </li>
        <li>
          <svg viewBox="0 0 16 16" aria-hidden="true"><path d="M1 3h14v10H1z M2.5 4.5 8 9l5.5-4.5" fill="none" stroke="#2F74B8" stroke-width="1.6"/></svg>
          <span>info@corvathproperties.com</span>
        </li>
        <li>
          <svg viewBox="0 0 16 16" aria-hidden="true"><g fill="none" stroke="#2F74B8" stroke-width="1.4"><circle cx="8" cy="8" r="6.5"/><ellipse cx="8" cy="8" rx="2.8" ry="6.5"/><path d="M1.5 8h13"/></g></svg>
          <span>www.corvathproperties.com</span>
        </li>
        <li>
          <svg viewBox="0 0 16 16" aria-hidden="true"><path d="M8 1a5 5 0 0 1 5 5c0 3.5-5 9-5 9S3 9.5 3 6a5 5 0 0 1 5-5zm0 3a2 2 0 1 0 0 4 2 2 0 0 0 0-4z"/></svg>
          <span>24 Harlow Street, Eastmere<br>P.O Box 4120 Westvale</span>
        </li>
      </ul>
    </div>
  </section>

</main>
</body>
</html>
```